App for Basket Haven to Link to Our Site and do simple things

After Simple design that acts as an interface for our customers. the app does simple things.

*Links to our Webpage - www.baskethaven.com.au
Shopping cart will live on our website

*People can call us from App - 1800 742 918
*People can send us a message from App
*We can Send Push Notifications
*Page dedicated to specials

*Link to Diary/Calendar (or create a inbuilt calendar) to remind people of upcoming birthdays/Anniversaries*** Reminder set 7 to 15 days before event to give enough time to send a gift.

Target Market(s)

People can download the app so they have our details handy on their phone

Industry/Entity Type

Retail

Colors

Designer to choose colors to be used in the design.

Requirements
Must have
• *** PREFER AN APP DESIGNER WHO CAN CODE THE APP AS WELL***
• Link to Diary/Calendar (or create a inbuilt calendar) to remind people of upcoming birthdays/Anniversaries*** Reminder set 7 to 15 days before event to give enough time to send a gift.
• Need to be able to send push notifications with special coupon codes
• Need to be able to send Push notifications
• Our Logo/as it or modified
• a map for directions 518 Tallowgate Road, West Brunswick VIC 3055
• Need to be able to change the Banner as needed

```html
<!DOCTYPE html>
<html lang="en">
<head>
<meta charset="utf-8">
<title>Basket Haven – Login page</title>
<link rel="stylesheet" href="https://fonts.googleapis.com/css2?family=Roboto:wght@300;400;700&family=Open+Sans:wght@400&display=swap">
<style>
  :root {
    --board-green: #428946;
    --label-white: #ffffff;
    --ink-dark: #152530;
    --status-ink: #1b1b1b;
    --field-fill: rgba(120, 112, 108, 0.55);
    --field-hint: rgba(235, 230, 228, 0.55);
    --soft-white: rgba(255, 255, 255, 0.92);
  }
  * { margin: 0; padding: 0; box-sizing: border-box; }
  html, body { width: 1200px; height: 1200px; overflow: hidden; }
  body {
    background: var(--board-green);
    position: relative;
    font-family: "Roboto", sans-serif;
  }
  .screen {
    position: absolute;
    left: 157px; top: 96px;
    width: 529px; height: 938px;
    overflow: hidden;
  }
  .screen-backdrop {
    position: absolute; inset: 0;
    background:
      radial-gradient(ellipse 55% 30% at 35% 52%, rgba(200,180,168,0.85), transparent 70%),
      radial-gradient(ellipse 50% 30% at 80% 55%, rgba(185,182,192,0.7), transparent 70%),
      radial-gradient(ellipse 60% 25% at 70% 95%, rgba(168,150,135,0.8), transparent 70%),
      linear-gradient(180deg, #f4f6f7 0%, #eceef0 18%, #d2cfd2 38%, #c4b8b3 55%, #ada4a0 72%, #979089 85%, #a49a90 100%);
  }
  .status-bar {
    position: absolute; left: 0; top: 0; width: 100%; height: 34px;
    font-family: "Open Sans", sans-serif; font-size: 16px; color: var(--status-ink);
  }
  .status-carrier { position: absolute; left: 10px; top: 6px; display: flex; align-items: center; gap: 6px; }
  .status-time { position: absolute; left: 0; right: 0; top: 6px; text-align: center; }
  .status-battery { position: absolute; right: 10px; top: 6px; display: flex; align-items: center; gap: 6px; }
  .brand {
    position: absolute; left: 80px; top: 250px;
    color: var(--ink-dark);
  }
  .brand-name {
    display: flex; align-items: center; gap: 12px;
    font-weight: 700; font-size: 34px; letter-spacing: 0.5px; text-transform: uppercase;
  }
  .brand-mark { width: 20px; height: 20px; background: var(--ink-dark); }
  .brand-phone {
    margin-top: 4px; margin-left: 70px;
    font-size: 20px; letter-spacing: 4px; font-weight: 400;
  }
  .login-form {
    position: absolute; left: 72px; top: 548px; width: 385px;
    text-align: center;
  }
  .login-title { font-weight: 300; font-size: 40px; color: var(--soft-white); line-height: 1; }
  .login-field {
    display: block; width: 100%; height: 47px; margin-top: 9px;
    background: var(--field-fill);
    color: var(--field-hint); font-family: "Roboto", sans-serif; font-weight: 300; font-size: 19px;
    text-align: left; padding-left: 18px; line-height: 47px;
  }
  .login-field:first-of-type { margin-top: 18px; }
  .forgot-link {
    text-align: right; padding-right: 5px; margin-top: 3px;
    font-weight: 300; font-size: 16px; color: rgba(240,238,236,0.75);
  }
  .signup-link { margin-top: 22px; font-size: 24px; font-weight: 400; color: var(--soft-white); }
  .screen-label {
    position: absolute; left: 772px; top: 540px;
    font-family: "Open Sans", sans-serif; font-size: 38px; color: var(--label-white);
  }
</style>
</head>
<body>
  <section class="screen">
    <div class="screen-backdrop" role="img" aria-label="Softly blurred background photo of gift hampers in warm beige and grey tones"></div>

    <div class="status-bar">
      <div class="status-carrier">
        <svg width="66" height="12" viewBox="0 0 66 12" aria-hidden="true">
          <circle cx="6" cy="6" r="5" fill="#1b1b1b"/>
          <circle cx="19" cy="6" r="5" fill="#1b1b1b"/>
          <circle cx="32" cy="6" r="5" fill="#1b1b1b"/>
          <circle cx="45" cy="6" r="4.4" fill="none" stroke="#1b1b1b" stroke-width="1.2"/>
          <circle cx="58" cy="6" r="4.4" fill="none" stroke="#1b1b1b" stroke-width="1.2"/>
        </svg>
        <span>Carrier</span>
        <svg width="22" height="16" viewBox="0 0 22 16" aria-hidden="true" style="margin-left:10px">
          <path d="M2 5 A13 13 0 0 1 20 5" fill="none" stroke="#1b1b1b" stroke-width="2.4"/>
          <path d="M5.5 8.5 A8 8 0 0 1 16.5 8.5" fill="none" stroke="#1b1b1b" stroke-width="2.4"/>
          <circle cx="11" cy="13" r="2.2" fill="#1b1b1b"/>
        </svg>
      </div>
      <div class="status-time">8:08 AM</div>
      <div class="status-battery">
        <span>50%</span>
        <svg width="40" height="16" viewBox="0 0 40 16" aria-hidden="true">
          <rect x="1" y="1" width="34" height="14" rx="2" fill="none" stroke="#1b1b1b" stroke-width="1.4"/>
          <rect x="3" y="3" width="15" height="10" fill="#1b1b1b"/>
          <rect x="36" y="5" width="3" height="6" fill="#1b1b1b"/>
        </svg>
      </div>
    </div>

    <div class="brand">
      <div class="brand-name"><span class="brand-mark"></span>Basket Haven</div>
      <div class="brand-phone">Call 1800 742 918</div>
    </div>

    <form class="login-form">
      <h1 class="login-title">Login</h1>
      <span class="login-field">User name</span>
      <span class="login-field">Password</span>
      <p class="forgot-link">forget password</p>
      <p class="signup-link">sign up</p>
    </form>
  </section>

  <p class="screen-label">Login page</p>
</body>
</html>
```